ebook cover for The Heron & The Marigold (Zing!)

We would like an ebook cover for a post Ph.D. on Animal Totems book called The Heron and The Marigold. It is about human relationships and dating. Author is Marta Lindqvist Ph.D.
I am thinking perhaps just typographic with a fancy custom italicized or handwriting kind of font that fills the whole page, or a picture that doesn't belittle the fairytale of love. Something cosmic.
The subtitle to guide people, small, is "on dating"

```html
<!DOCTYPE html>
<html lang="en">
<head>
<meta charset="utf-8">
<title>The Heron and The Marigold — On Dating</title>
<link rel="stylesheet" href="https://fonts.googleapis.com/css2?family=Kaushan+Script&family=Josefin+Sans:wght@400&display=swap">
<style>
  :root {
    --canvas: #ffffff;
    --paper: #fdf8e3;
    --red: #fe0000;
    --heart-tone: #f6b7b4;
    --band-text: #ffffff;
  }
  * { margin: 0; padding: 0; box-sizing: border-box; }
  html, body {
    width: 1200px;
    height: 1200px;
    overflow: hidden;
    background: var(--canvas);
  }
  .cover {
    position: absolute;
    left: 230px;
    top: 0;
    width: 762px;
    height: 1200px;
    background: var(--paper);
    overflow: hidden;
  }
  .title-word {
    position: absolute;
    font-family: "Kaushan Script", cursive;
    color: var(--red);
    line-height: 1;
    white-space: nowrap;
  }
  .title-the-top {
    left: 335px;
    top: 40px;
    font-size: 150px;
    transform: rotate(-6deg);
  }
  .title-heron {
    left: 30px;
    top: 170px;
    font-size: 230px;
    transform: rotate(-6deg);
  }
  .title-and-the {
    left: 200px;
    top: 430px;
    font-size: 130px;
    transform: rotate(-5deg);
  }
  .title-marigold {
    left: 22px;
    top: 590px;
    font-size: 178px;
    transform: rotate(-5deg);
  }
  .subtitle {
    position: absolute;
    left: 120px;
    top: 880px;
    font-family: "Kaushan Script", cursive;
    font-size: 70px;
    line-height: 1;
    color: var(--red);
    transform: rotate(-4deg);
  }
  .heart-art {
    position: absolute;
    left: 555px;
    top: 835px;
    width: 130px;
    height: 115px;
  }
  .author-band {
    position: absolute;
    left: 0;
    top: 1068px;
    width: 762px;
    height: 96px;
    background: var(--red);
    display: flex;
    align-items: center;
    justify-content: center;
  }
  .author-name {
    font-family: "Josefin Sans", sans-serif;
    font-weight: 400;
    font-size: 48px;
    letter-spacing: 0.16em;
    color: var(--band-text);
    text-transform: uppercase;
    white-space: nowrap;
    padding-top: 8px;
  }
</style>
</head>
<body>
  <main class="cover">
    <h1 class="title">
      <span class="title-word title-the-top">The</span>
      <span class="title-word title-heron">Heron</span>
      <span class="title-word title-and-the">and The</span>
      <span class="title-word title-marigold">Marigold</span>
    </h1>
    <p class="subtitle">On Dating</p>
    <svg class="heart-art" viewBox="0 0 130 115" role="img" aria-label="Hand-drawn red crayon heart">
      <rect x="0" y="0" width="130" height="115" rx="40" fill="var(--heart-tone)" opacity="0.55"/>
    </svg>
    <div class="author-band">
      <p class="author-name">Marta Lindqvist Ph.D</p>
    </div>
  </main>
</body>
</html>
```